Velmor Partners - website for real estate investment company

Create a bold, modern website that reflects Velmor’s success, professionalism, and credibility.
The design must stand out while maintaining a polished, corporate tone. (bold, but understated)
The client just created a new logo, and the website design must be in sync with the logo design. Information about the logo colors, fonts, and message are in the attached design brief.

Target Market(s)

b2b: banks, brokers, institutional partners, vendors, and property sellers.

Industry/Entity Type

real estate investment company

Number of Pages Required

1 page

Font styles to use
Sans Serif

Colors

Designer to choose colors to be used in the design.

Requirements
Must have
• 1. homepage design (psd) 2. a top banner image (psd) for a default inner page
Nice to have
• please see attached design brief
Should not have

```html
<!DOCTYPE html>
<html lang="en">
<head>
<meta charset="utf-8">
<title>Velmor Partners</title>
<link href="https://fonts.googleapis.com/css2?family=Oswald:wght@300;400;500;600;700&family=Barlow:wght@400;500;600;700&family=Instrument+Sans:wght@400;500&display=swap" rel="stylesheet">
<style>
:root{
  --red:#d8202a;
  --red-deep:#b41e25;
  --ink:#2b2b2b;
  --grey-band:#4a4a4a;
  --panel:#3d3d3d;
  --light:#f5f5f5;
  --ghost:#efefef;
  --white:#ffffff;
  --muted:#666;
}
*{margin:0;padding:0;box-sizing:border-box}
html,body{width:1200px;height:3157px;overflow:hidden;background:var(--white)}
body{position:relative;font-family:"Barlow",sans-serif;color:var(--ink)}
.abs{position:absolute}
.display{font-family:"Oswald",sans-serif;text-transform:uppercase;line-height:1}

/* hero */
.hero{left:0;top:0;width:1200px;height:728px;
  background:linear-gradient(180deg,#1b2740 0%,#3a4a66 18%,#6b5a4f 30%,#2c3550 45%,#1d2d4e 62%,#1a2a48 100%)}
.hero-glow{left:0;top:250px;width:1200px;height:200px;background:radial-gradient(ellipse at 50% 50%,rgba(230,170,80,.35),rgba(0,0,0,0) 70%)}
.logo{font-family:"Barlow",sans-serif;font-weight:700;color:var(--white);letter-spacing:1px;display:flex;align-items:center;gap:8px}
.logo .mark{width:12px;height:12px;background:var(--red)}
.nav{left:280px;top:40px;display:flex;gap:25px;font-size:13.5px;font-weight:700;color:var(--white);text-transform:uppercase}
.nav .active{position:relative;padding-left:4px}
.nav .active::before{content:"";position:absolute;left:0;top:-1px;width:7px;height:7px;background:var(--red);clip-path:polygon(0 0,100% 0,0 100%)}
.nav-cta{left:930px;top:22px;width:184px;height:50px;background:var(--red);clip-path:polygon(0 0,100% 0,80% 100%,0 100%);color:var(--white);font-weight:700;font-size:14px;display:flex;align-items:center;padding-left:45px}
.hero-title{left:0;top:375px;width:1200px;text-align:center;font-weight:300;font-size:86px;color:var(--white);letter-spacing:-1px}

/* story */
.ghost{font-family:"Oswald",sans-serif;font-weight:700;color:var(--ghost);text-transform:uppercase;line-height:1}
.corner{width:22px;height:22px;background:var(--red);clip-path:polygon(0 0,100% 0,0 100%)}
.section-title{font-size:72px;font-weight:300;color:var(--ink)}
.section-title b{font-weight:700}
.story-text{left:530px;top:913px;width:590px;font-family:"Instrument Sans",sans-serif;font-size:23px;line-height:32px;color:#222}
.stat{top:1105px}
.stat .num{font-family:"Oswald",sans-serif;font-weight:600;font-size:62px;line-height:1;color:var(--ink)}
.stat .lbl{font-family:"Oswald",sans-serif;font-weight:300;font-size:16px;line-height:22px;color:#333;margin-top:12px;padding-left:4px}
.divider{width:1px;height:92px;background:#ccc;top:1115px}

/* gallery */
.gallery{left:0;top:1355px;width:1200px;height:657px;background:var(--grey-band)}
.shot{top:1426px;width:331px;height:529px}

/* reviews */
.reviews{left:0;top:2012px;width:1200px;height:673px;background:var(--light)}
.card{top:2272px;width:394px;height:261px;background:var(--white);border-radius:6px;padding:24px 28px}
.stars{color:var(--ink);font-size:17px;letter-spacing:2px}
.card h3{font-family:"Barlow",sans-serif;font-weight:500;font-size:21px;margin-top:4px}
.card p{font-family:"Instrument Sans",sans-serif;font-size:14px;line-height:21px;color:#555;margin-top:14px}
.who{display:flex;align-items:center;gap:10px;margin-top:22px}
.avatar{width:42px;height:42px;border-radius:50%;background:#c9ccd2}
.who b{display:block;font-weight:500;font-size:16px}
.who span{font-size:12px;color:var(--muted)}
.arrow-btn{top:2122px;width:43px;height:43px;display:flex;align-items:center;justify-content:center}

/* footer */
.foot-red{left:0;top:2685px;width:750px;height:472px;background:var(--red-deep)}
.foot-panel{left:750px;top:2622px;width:450px;height:535px;background:var(--panel)}
.career{left:97px;top:2924px;width:232px;height:50px;background:var(--white);clip-path:polygon(0 0,100% 0,83% 100%,0 100%);color:var(--red);font-weight:700;font-size:14px;display:flex;align-items:center;padding-left:32px;gap:6px}
.foot-h{font-family:"Oswald",sans-serif;font-weight:700;font-size:58px;color:var(--white);text-transform:uppercase;line-height:1}
.foot-t{font-family:"Oswald",sans-serif;font-weight:500;font-size:24px;line-height:29px;color:var(--white)}
.field{left:795px;width:301px;border:1px solid #6a6a6a;color:var(--white);font-size:17px;display:flex;align-items:flex-start;gap:10px;padding:14px 10px}
.submit{left:796px;top:2998px;width:298px;height:50px;background:var(--red);clip-path:polygon(0 0,100% 0,86% 100%,0 100%);color:var(--white);font-weight:700;font-size:14px;display:flex;align-items:center;justify-content:center;padding-right:30px}
.copy{left:85px;top:3095px;font-size:13px;font-weight:500;color:rgba(255,255,255,.8)}
.copy b{color:var(--white)}
</style>
</head>
<body>

<!-- hero -->
<div class="abs hero" role="img" aria-label="Night skyline of a waterfront city at dusk"></div>
<div class="abs hero-glow"></div>
<div class="abs logo" style="left:83px;top:28px;font-size:46px"><span class="mark"></span>VELMOR</div>
<nav class="abs nav">
  <span class="active">Home</span><span>Our Story</span><span>Investment Strategy</span><span>What Sets Us Apart</span><span>Our Portfolio</span>
</nav>
<div class="abs nav-cta">CONTACT</div>
<svg class="abs" style="left:535px;top:230px" width="130" height="130" viewBox="0 0 130 130">
  <defs><path id="ring" d="M65,65 m-46,0 a46,46 0 1,1 92,0 a46,46 0 1,1 -92,0"/></defs>
  <text font-family="Barlow,sans-serif" font-size="13" font-weight="700" fill="#fff" letter-spacing="9"><textPath href="#ring" startOffset="4%">WATCH • OUR VIDEO •</textPath></text>
  <path d="M55,48 L80,64 L55,80 Z" fill="none" stroke="#d8202a" stroke-width="3"/>
</svg>
<div class="abs display hero-title">Experience · Strategy · Vision</div>

<!-- story -->
<div class="abs ghost" style="left:122px;top:742px;font-size:150px">Our Story</div>
<div class="abs corner" style="left:573px;top:752px"></div>
<div class="abs corner" style="left:128px;top:848px"></div>
<div class="abs display section-title" style="left:132px;top:842px">Our <b>Story</b></div>
<svg class="abs" style="left:86px;top:934px" width="425" height="395" viewBox="0 0 425 395">
  <polygon points="0,0 384,0 200,190 0,395" fill="#b41e25"/>
</svg>
<div class="abs" role="img" aria-label="Modern two-storey white villa with glass walls" style="left:100px;top:978px;width:408px;height:328px;background:linear-gradient(160deg,#f4f4f2 0%,#d9d8d4 45%,#6d6a63 75%,#2f3a2c 100%);clip-path:polygon(45% 0,100% 30%,100% 92%,50% 100%,0 88%,0 30%)"></div>
<p class="abs story-text">Velmor Partners is a vertically integrated real estate investment firm with a proven four-decade track record. We acquire, reposition, and operate high-performing assets across multiple sectors — always with a focus on exceptional, risk-adjusted returns.</p>
<div class="abs stat" style="left:522px"><div class="num">1989</div><div class="lbl">Founded</div></div>
<div class="abs divider" style="left:675px"></div>
<div class="abs stat" style="left:710px"><div class="num">23,000+</div><div class="lbl">Multifamily &amp; healthcare units</div></div>
<div class="abs divider" style="left:935px"></div>
<div class="abs stat" style="left:975px"><div class="num">$300+</div><div class="lbl">Million invested in<br>renovations</div></div>

<!-- gallery -->
<div class="abs gallery"></div>
<div class="abs shot" style="left:85px;background:linear-gradient(180deg,#5d8fd0 0%,#a9c6e6 40%,#7f8a93 65%,#3b4048 100%)" role="img" aria-label="Tall residential tower rising over a dense city"></div>
<div class="abs shot" style="left:435px;background:linear-gradient(180deg,#c9c9c9 0%,#e8e8e6 45%,#9a9894 60%,#d4d3cf 100%)" role="img" aria-label="Marble elevator lobby corridor"></div>
<svg class="abs" style="left:572px;top:1664px" width="56" height="56" viewBox="0 0 56 56" fill="none" stroke="#fff" stroke-width="3">
  <path d="M32 24 L50 6 M38 6 H50 V18 M24 32 L6 50 M6 38 V50 H18"/>
</svg>
<div class="abs shot" style="left:784px;background:linear-gradient(180deg,#d9a66a 0%,#c8925c 35%,#7d6a58 60%,#3b3530 100%)" role="img" aria-label="Skyline with a classic spire tower at sunset"></div>

<!-- reviews -->
<div class="abs reviews"></div>
<div class="abs ghost" style="left:360px;top:2070px;font-size:140px;color:#e9e9e9">Client</div>
<div class="abs corner" style="left:818px;top:2082px"></div>
<div class="abs ghost" style="left:690px;top:2535px;font-size:140px;color:#e9e9e9">Review</div>
<div class="abs corner" style="left:85px;top:2104px;width:40px;height:40px"></div>
<div class="abs display section-title" style="left:100px;top:2106px;line-height:70px">What our<br><b>client say...</b></div>
<div class="abs arrow-btn" style="left:1017px;border:1px solid #bbb;background:var(--white)">
  <svg width="30" height="12" viewBox="0 0 30 12" fill="none" stroke="#333" stroke-width="1.5"><path d="M29 6H1M6 1L1 6L6 11"/></svg>
</div>
<div class="abs arrow-btn" style="left:1092px;background:var(--red)">
  <svg width="30" height="12" viewBox="0 0 30 12" fill="none" stroke="#fff" stroke-width="1.5"><path d="M1 6H29M24 1L29 6L24 11"/></svg>
</div>

<div class="abs card" style="left:85px">
  <div class="stars">★★★★★</div><h3>Highly recommend!</h3>
  <p>Lorem ipsor sit amet, consectetur adipiscing elit, sed do eiusmod tempor incididunt ut labore et dolore magna aliqua. Quis ipsum suspendisse ulces gravida. Maecenas lectus metus, gravida sed.</p>
  <div class="who"><span class="avatar"></span><div><b>Daniel Reyes</b><span>Client</span></div></div>
</div>
<div class="abs card" style="left:512px">
  <div class="stars">★★★★★</div><h3>Very happy to connect with Velmor</h3>
  <p>Lorem ipsor sit amet, consectetur adipiscing elit, sed do eiusmod tempor incididunt ut labore et dolore magna aliqua. Quis ipsum suspendisse ulces gravida. Maecenas lectus metus, gravida sed.</p>
  <div class="who"><span class="avatar"></span><div><b>Clara Benton</b><span>Client</span></div></div>
</div>
<div class="abs card" style="left:939px">
  <div class="stars">★★★★★</div><h3>Highly recommend!</h3>
  <p>Lorem ipsor sit amet, consectetur adipiscing elit, sed do eiusmod tempor incididunt ut labore et dolore magna aliqua. Quis ipsum suspendisse ulces gravida. Maecenas lectus metus, gravida sed.</p>
  <div class="who"><span class="avatar"></span><div><b>Nora Kellan</b><span>Client</span></div></div>
</div>

<!-- footer -->
<div class="abs foot-red"></div>
<div class="abs foot-panel"></div>
<div class="abs logo" style="left:86px;top:2812px;font-size:70px"><span class="mark" style="width:16px;height:16px"></span>VELMOR</div>
<div class="abs career">
  <svg width="14" height="11" viewBox="0 0 14 11"><rect x="0" y="0" width="14" height="11" fill="#d8202a"/><path d="M0 0L7 6L14 0" fill="none" stroke="#fff" stroke-width="1.3"/></svg>
  CAREER INQUIRIES
</div>
<div class="abs foot-h" style="left:439px;top:2792px">Location</div>
<div class="abs foot-t" style="left:439px;top:2858px">2140 Harbor Ave, Linden,<br>NJ 07036</div>
<div class="abs foot-h" style="left:439px;top:2950px">Contact Us</div>
<div class="abs foot-t" style="left:439px;top:3012px">info@velmor.com</div>

<div class="abs corner" style="left:795px;top:2694px;background:var(--red)"></div>
<div class="abs display section-title" style="left:800px;top:2696px;font-size:58px;color:var(--white)">Get in <b>Touch</b></div>
<div class="abs field" style="top:2766px;height:52px">
  <svg width="14" height="16" viewBox="0 0 14 16" fill="#999"><circle cx="7" cy="4.5" r="4"/><path d="M0 16C0 11 3 9 7 9S14 11 14 16Z"/></svg>Name</div>
<div class="abs field" style="top:2829px;height:52px">
  <svg width="15" height="11" viewBox="0 0 15 11"><rect width="15" height="11" fill="#999"/><path d="M0 0L7.5 6L15 0" fill="none" stroke="#3d3d3d" stroke-width="1.3"/></svg>Email</div>
<div class="abs field" style="top:2892px;height:95px">
  <svg width="15" height="15" viewBox="0 0 15 15" fill="none" stroke="#999" stroke-width="1.5"><path d="M8 2H1V14H13V7"/><path d="M6 9L14 1"/></svg>Message</div>
<div class="abs submit">SUBMIT</div>

<div class="abs copy">© 2025 <b>VELMOR PARTNERS</b>. ALL RIGHT RESERVED</div>

</body>
</html>
```